Harbor Sprig small batch hot sauce label project

I am launching a line of small batch sauces (hot sauces, bbq sauces) and I need a label for my bottles. I have a logo that I like, I'm not completely married to it but It is a good logo. I would like the name of my business and the name of the sauce on the label. Something fun, edgy that would make you want to pick it up off the shelf.

Target Market(s)

Milennials, food bloggers, stay at home moms who want to amp up their dishes with a really good sauce

Industry/Entity Type

Cooking

Requirements
Must have
• I am open to interpretation
Nice to have
• Maybe a bomb cloud since I want to go in the sauce bomb direction.

```html
<!DOCTYPE html>
<html lang="en">
<head>
<meta charset="utf-8">
<title>Harbor Sprig Hot Sauce Label</title>
<link rel="stylesheet" href="https://fonts.googleapis.com/css2?family=Bebas+Neue&family=Kaushan+Script&family=Montserrat:wght@500&display=swap">
<style>
  :root {
    --page: #ffffff;
    --paper: #ebe7df;
    --paper-edge: #cbc1b2;
    --rust: #b04a2f;
    --rust-band: #b8583f;
    --rust-soft: #c46a4f;
    --tan: #a99a85;
    --ink: #1c1a18;
    --cream: #efe9de;
  }
  * { margin: 0; padding: 0; box-sizing: border-box; }
  html, body {
    width: 1200px; height: 1200px; overflow: hidden;
    background: var(--page);
  }
  .label {
    position: absolute;
    left: 82px; top: 30px;
    width: 1037px; height: 1140px;
    background: radial-gradient(ellipse at 60% 45%, var(--paper) 0%, #e2dcd1 55%, var(--paper-edge) 100%);
    overflow: hidden;
  }
  .edge-band {
    position: absolute; left: 0; width: 100%;
    background: var(--rust);
  }
  .edge-band--top { top: 0; height: 33px; }
  .edge-band--bottom { bottom: 0; height: 50px; }
  .brand-column {
    position: absolute; left: 251px; top: 33px;
    width: 254px; height: 1057px;
    background: var(--tan);
  }
  .brand-column__cap {
    position: absolute; left: 0; top: 0;
    width: 100%; height: 205px;
    background: var(--rust-band);
  }
  .brand-mark {
    position: absolute; left: 322px; top: 82px;
    width: 110px; height: 110px;
    background: var(--cream);
  }
  .brand-name {
    position: absolute; left: 533px; top: 66px;
    font-family: "Bebas Neue", sans-serif;
    font-size: 66px; line-height: 0.92;
    letter-spacing: 3px;
    color: var(--ink);
    text-transform: uppercase;
  }
  .bomb-art {
    position: absolute; left: 110px; top: 240px;
    width: 400px; height: 690px;
    background: linear-gradient(180deg, var(--rust-soft) 0%, var(--rust) 100%);
  }
  .hot {
    position: absolute; left: 110px; width: 400px; top: 440px;
    text-align: center;
    font-family: "Bebas Neue", sans-serif;
    font-size: 220px; line-height: 1;
    color: var(--cream);
    letter-spacing: -4px;
  }
  .product {
    position: absolute; left: 520px; width: 420px;
    text-align: center;
  }
  .product__name {
    top: 700px;
    font-family: "Bebas Neue", sans-serif;
    font-size: 190px; line-height: 1;
    color: var(--ink);
    letter-spacing: -3px;
  }
  .product__variant {
    top: 882px;
    font-family: "Kaushan Script", cursive;
    font-size: 86px; line-height: 1;
    color: var(--rust);
  }
  .product__note {
    top: 1016px;
    font-family: "Montserrat", sans-serif;
    font-weight: 500;
    font-size: 29px;
    color: var(--ink);
  }
  .net-weight {
    position: absolute; left: 251px; width: 254px; top: 1034px;
    text-align: center;
    font-family: "Montserrat", sans-serif;
    font-weight: 500;
    font-size: 26px;
    color: var(--ink);
  }
</style>
</head>
<body>
  <main class="label">
    <div class="edge-band edge-band--top"></div>
    <div class="brand-column">
      <div class="brand-column__cap"></div>
    </div>
    <div class="brand-mark" aria-hidden="true"></div>
    <p class="brand-name">Harbor<br>Sprig</p>

    <div class="bomb-art" role="img" aria-label="Illustration of a lit cartoon bomb bursting out of a rust-coloured explosion cloud with halftone dots"></div>
    <p class="hot">HOT</p>

    <p class="product product__name">SAUCE</p>
    <p class="product product__variant">original</p>
    <p class="product product__note">- SMALL BATCH -</p>
    <p class="net-weight">16 OZ</p>

    <div class="edge-band edge-band--bottom"></div>
  </main>
</body>
</html>
```